Brenvoke Professional Jewellery Polishers
Dunmere - Ashgrove Quarter (Optional)
No
We are professional jewellery polishers based in London's Hatton Garden. We currently provide many high-end retailers with high quality jewellery polishing, but we are now aiming to target the general public offering cheap jewellery polishing.
We want to convey an impression that we are a trustworthy and professional team of jewellers that provide high quality jewellery polishing (and other jewellery workshop services) whilst being able to offer very reasonable prices.
Our website is currently under constructions - however I have provided the websites to 3 other companies that are very similar to us (The 1st URL being the most useful).
http://www.tqlustreworks.co.uk/services/jewellery-polishing/
http://hwardellow.co.uk/services-we-provide
http://www.velmontique.com/services/client-services/after-sales-service/after-sales-service-jewelry/-58316
http://nukeshiners.co.uk/
Professional
Completely up to yourself
not sure
Please could you put emphasis on the 'Professional Jewellery Polishers' part.
If you feel like the logo would look better without 'Dunmere - Ashgrove Quarter' then please feel free to remove it.
For the brochure:
- I have seen a few brochures in black and have found them quite intriguing. Feel free to play with black shades, or have a black background.
- More importantly I would like the brochure to be as attractive as possible, whist looking sophisticated and affordable. Please feel free to use what colour you feel would achieve this best.
- We would prefer a landscape/ horizontal brochure, but we would not disregard a portrait style brochure.

```html
<!DOCTYPE html>
<html lang="en">
<head>
<meta charset="utf-8">
<title>Brenvoke Professional Jewellery Polishers – Business Card</title>
<link rel="stylesheet" href="https://fonts.googleapis.com/css2?family=Cinzel:wght@400;600&family=Oswald:wght@300&family=Lato:wght@400&display=swap">
<style>
  :root {
    --backdrop: #e8e3db;
    --card-dark: #2b2b2d;
    --card-dark-edge: #1f1f21;
    --gold: #c9a54a;
    --gold-light: #f0d98a;
    --gold-deep: #8a6a22;
    --silver: #e4e1d8;
    --ink-light: #f3f1ec;
    --ink-muted: #c8c4bb;
  }
  * { margin: 0; padding: 0; box-sizing: border-box; }
  html, body { width: 1200px; height: 751px; overflow: hidden; }
  body { background: var(--backdrop); position: relative; font-family: "Lato", sans-serif; }

  .card {
    position: absolute;
    border-radius: 9px;
    overflow: hidden;
    background: radial-gradient(ellipse at 40% 30%, #343436 0%, var(--card-dark) 55%, var(--card-dark-edge) 100%);
    box-shadow: 0 6px 18px rgba(0,0,0,0.28);
  }
  .card--front { left: 376px; top: 113px; width: 448px; height: 247px; }
  .card--back  { left: 376px; top: 379px; width: 450px; height: 257px; }

  .wordmark { position: absolute; text-align: center; color: var(--gold); font-family: "Oswald", sans-serif; font-weight: 300; }
  .wordmark__dot { display: block; margin: 0 auto 8px; border-radius: 50%; background: var(--gold); }
  .wordmark__name { display: block; text-transform: uppercase; letter-spacing: 0.5px; white-space: nowrap; }
  .wordmark__tag { display: block; letter-spacing: 3px; white-space: nowrap; }

  .card--front .wordmark { left: 0; right: 0; top: 50px; }
  .card--front .wordmark__dot { width: 40px; height: 40px; margin-bottom: 24px; }
  .card--front .wordmark__name { font-size: 25px; line-height: 1; }
  .card--front .wordmark__tag { font-size: 13px; margin-top: 6px; }

  .location {
    position: absolute; left: 0; right: 0; top: 211px;
    text-align: center; font-family: "Cinzel", serif; font-size: 8px;
    letter-spacing: 3px; color: var(--ink-muted);
  }
  .gold-band {
    position: absolute; left: 0; right: 0; bottom: 0;
    background: linear-gradient(180deg, var(--gold-light) 0%, var(--gold) 40%, var(--gold-deep) 100%);
  }
  .card--front .gold-band { height: 18px; }

  .holder-name {
    position: absolute; right: 22px; top: 46px;
    font-family: "Cinzel", serif; font-weight: 400; font-size: 19px; letter-spacing: 1px; color: var(--ink-light);
  }
  .gold-rule {
    position: absolute; left: 0; right: 0; top: 76px; height: 3px;
    background: linear-gradient(90deg, rgba(201,165,74,0) 0%, var(--gold) 45%, var(--gold-light) 100%);
  }
  .card--back .wordmark { left: 14px; width: 180px; top: 108px; }
  .card--back .wordmark__dot { width: 30px; height: 30px; margin-bottom: 12px; }
  .card--back .wordmark__name { font-size: 17px; line-height: 1; }
  .card--back .wordmark__tag { font-size: 9px; margin-top: 4px; letter-spacing: 2px; }

  .contact-list {
    position: absolute; right: 16px; top: 106px; list-style: none;
    font-size: 7.5px; color: var(--ink-muted); text-align: right; line-height: 13px;
  }
  .contact-list li { display: flex; justify-content: flex-end; align-items: center; gap: 6px; white-space: nowrap; }
  .contact-list li.gap { margin-top: 6px; }
  .contact-list .icon { width: 8px; height: 8px; flex: none; }
  .contact-list .icon--blank { visibility: hidden; }

  .card--back .gold-band {
    height: 30px;
    background: linear-gradient(180deg, var(--silver) 0%, #cfc7b0 35%, var(--gold) 70%, var(--gold-deep) 100%);
  }
</style>
</head>
<body>

<section class="card card--front" aria-label="Business card front">
  <div class="wordmark">
    <span class="wordmark__dot"></span>
    <span class="wordmark__name">Brenvoke Professional</span>
    <span class="wordmark__tag">Jewellery Polishers</span>
  </div>
  <p class="location">DUNMERE · ASHGROVE QUARTER</p>
  <div class="gold-band"></div>
</section>

<section class="card card--back" aria-label="Business card back">
  <h1 class="holder-name">Rohan Belcastle</h1>
  <div class="gold-rule"></div>

  <div class="wordmark">
    <span class="wordmark__dot"></span>
    <span class="wordmark__name">Brenvoke Professional</span>
    <span class="wordmark__tag">Jewellery Polishers</span>
  </div>

  <ul class="contact-list">
    <li>0774 210 5583
      <svg class="icon" viewBox="0 0 10 10"><rect x="3" y="0.5" width="4" height="9" rx="1" fill="none" stroke="#c8c4bb" stroke-width="1"/></svg></li>
    <li>0207 318 4461
      <svg class="icon" viewBox="0 0 10 10"><path d="M2 1 L4 1 L5 3 L4 4 Q5 6 6 6 L7 5 L9 6 L9 8 Q5 9 2 5 Q1 3 2 1Z" fill="#c8c4bb"/></svg></li>
    <li class="gap">www.brenvokepolishers.co.uk
      <svg class="icon" viewBox="0 0 10 10"><circle cx="5" cy="5" r="4" fill="none" stroke="#c8c4bb"/><path d="M1 5H9M5 1V9" stroke="#c8c4bb" stroke-width="0.8"/></svg></li>
    <li>www.brenvokeprofessional.co.uk
      <svg class="icon icon--blank" viewBox="0 0 10 10"></svg></li>
    <li class="gap">info@brenvokeprofessional.co.uk
      <svg class="icon" viewBox="0 0 10 10"><rect x="1" y="2.5" width="8" height="5.5" fill="none" stroke="#c8c4bb"/><path d="M1 2.5L5 6L9 2.5" fill="none" stroke="#c8c4bb"/></svg></li>
    <li class="gap">4th Floor, 18 Marwick Row,
      <svg class="icon" viewBox="0 0 10 10"><path d="M5 9.5 L2 5 A3 3 0 1 1 8 5 Z" fill="#c8c4bb"/></svg></li>
    <li>Ashgrove Quarter, Dunmere DN4 7QX
      <svg class="icon icon--blank" viewBox="0 0 10 10"></svg></li>
  </ul>

  <div class="gold-band"></div>
</section>

</body>
</html>
```